Web redesign for Asian (IndoPak) based private equity firm

Redesign TLKventures.com.
New site to be done on Wordpress. No flash, responsive. Keep logo. Home page, news, team, portfolio, contact us. Portfolio will be case study based so we will have some next about an industry like infrastructure and then Have logos below. Use existing images and others from Indian stock photo sites (will pay for those so use placeholders). Home page should have news feed and video front and center. Images should have eye contact. Looking for clean and simple design .

Sites we like
http://www.dmvh.com- use of video highlight

Leafly.in
A magazine that I find very easy to read and scroll down
Allows for both text /photo and video

Target Market(s)

Private equity

Industry/Entity Type

Financial Service

Coding

Coded - Design and coding required

Number of Pages Required

5+ page

Font styles to use
Serif
Sans Serif

Colors
3377b5
85acd3

Requirements
Must have
• Responsive, video highlight, image use, existing logo, contact us, open page design . Use existing color
Nice to have
• Connect news story to content on page using tags. Pop over for team bios, custom font
Should not have
• Flash, no need for inline CSS on the content pages except absolutely necessary. No rigid content types

```html
<!DOCTYPE html>
<html lang="en">
<head>
<meta charset="utf-8">
<title>TLK Ventures — Growth Capital</title>
<link href="https://fonts.googleapis.com/css2?family=Open+Sans:wght@400;600;700&family=Roboto+Condensed:wght@400;700&family=Noto+Serif:wght@400&display=swap" rel="stylesheet">
<style>
:root{
  --brand:#3377b5;
  --brand-light:#85acd3;
  --brand-deep:#1f5a92;
  --ink:#2a2a2a;
  --muted:#6b6b6b;
  --line:#e2e2e2;
  --footer:#232323;
  --footer-text:#a9a9a9;
  --white:#ffffff;
  --accent:#e0702c;
}
*{box-sizing:border-box;margin:0;padding:0}
html,body{width:1200px;height:2544px;overflow:hidden}
body{font-family:"Open Sans",Arial,sans-serif;color:var(--ink);background:var(--white);position:relative}
.hero{position:absolute;left:0;top:0;width:1200px;height:552px;overflow:hidden}
.hero-media{position:absolute;inset:0;background:linear-gradient(135deg,#4f8cc4 0%,#2f6ea9 45%,#6d9ccb 75%,#3a78b2 100%)}
.hero-media::after{content:"";position:absolute;inset:0;background:rgba(51,119,181,.35)}
.site-header{position:absolute;left:0;top:0;width:100%;height:110px;z-index:2}
.brand{position:absolute;left:40px;top:28px;display:flex;align-items:center;gap:10px;color:var(--white);font-family:"Roboto Condensed",sans-serif;font-weight:700;font-size:30px;letter-spacing:1px}
.brand-mark{width:14px;height:14px;background:var(--white)}
.main-nav{position:absolute;left:362px;top:42px;display:flex;gap:22px}
.main-nav a{color:var(--white);text-decoration:none;font-size:12px;font-weight:700;letter-spacing:.5px}
.utility{position:absolute;right:22px;top:36px;display:flex;gap:10px}
.utility a{display:block;padding:5px 12px;border:2px solid var(--white);color:var(--white);font-size:12px;font-weight:700;text-decoration:none;letter-spacing:.5px}
.hero-card{position:absolute;left:408px;top:180px;width:384px;height:240px;border:1px solid rgba(255,255,255,.7);z-index:2;text-align:center;color:var(--white)}
.hero-title{margin:12px auto 0;width:352px;height:48px;border:2px solid var(--white);font-family:"Roboto Condensed",sans-serif;font-weight:700;font-size:28px;letter-spacing:3px;line-height:44px}
.hero-text{margin:22px 30px 0;font-size:12.5px;line-height:19px}
.hero-btn{display:inline-block;margin-top:16px;padding:5px 12px;border:1px solid var(--white);font-size:10px;font-weight:700;letter-spacing:1px;color:var(--white);text-decoration:none}
.hero-dots{position:absolute;left:0;right:0;top:508px;display:flex;justify-content:center;gap:22px;z-index:2}
.hero-dots span{width:14px;height:14px;border-radius:50%;background:rgba(255,255,255,.6)}
.hero-dots span:first-child{background:var(--white)}
.section-head{position:absolute;left:56px;display:flex;align-items:center;gap:12px}
.section-icon{width:30px;height:30px;background:var(--brand);display:flex;align-items:center;justify-content:center}
.section-title{font-family:"Roboto Condensed",sans-serif;font-weight:700;font-size:26px;color:var(--ink)}
.latest{position:absolute;left:0;top:552px;width:1200px;height:420px;background:#f7f7f7;border-bottom:1px solid var(--line)}
.see-all{position:absolute;right:56px;top:68px;background:var(--ink);color:var(--white);font-size:10px;padding:3px 7px}
.latest-row{position:absolute;left:56px;top:128px;display:flex;gap:22px}
.latest-card{width:202px;background:var(--white);height:212px}
.thumb{display:block}
.latest-card .thumb{height:92px}
.latest-meta{font-size:10px;color:var(--accent);margin:8px 10px 4px}
.latest-text{font-family:"Noto Serif",serif;font-size:11.5px;line-height:16px;margin:0 10px;color:var(--ink)}
.news{position:absolute;left:0;top:972px;width:1200px;height:780px}
.news-grid{position:absolute;left:56px;top:160px;display:grid;grid-template-columns:548px 548px;column-gap:16px;row-gap:88px}
.news-item{display:flex;gap:16px;height:92px}
.news-item .thumb{width:112px;height:92px;flex:none;position:relative}
.news-grid .news-item:nth-child(even) .thumb{width:112px}
.news-text{font-family:"Noto Serif",serif;font-size:12px;line-height:18px;width:400px}
.play{position:absolute;left:40px;top:30px;width:32px;height:32px;border-radius:50%;background:#d63a2f;display:flex;align-items:center;justify-content:center}
.load-more{position:absolute;left:536px;top:718px;width:128px;height:32px;border:1px solid #bdbdbd;font-size:11px;font-weight:700;letter-spacing:1px;text-align:center;line-height:30px;color:var(--ink)}
.portfolio{position:absolute;left:0;top:1752px;width:1200px;height:408px;border-top:1px solid var(--line)}
.portfolio-row{position:absolute;left:80px;top:88px;display:flex;gap:0}
.company{width:208px;text-align:center}
.company-mark{height:120px;display:flex;align-items:center;justify-content:center;gap:8px;font-family:"Open Sans",sans-serif;font-weight:700;font-size:19px;color:var(--brand)}
.company-mark i{width:12px;height:12px;background:var(--brand);display:block}
.company-name{font-size:13px;font-weight:700;margin-top:12px;line-height:18px}
.company-sector{font-size:12px;color:var(--muted);margin-top:6px;line-height:17px}
.arrow{position:absolute;top:128px}
.social-bar{position:absolute;left:0;top:2160px;width:1200px;height:44px;background:var(--brand);display:flex}
.social-bar a{flex:1;color:var(--white);text-decoration:none;font-size:11px;font-weight:700;letter-spacing:.5px;text-align:center;line-height:44px;border-right:1px solid rgba(255,255,255,.25)}
.social-bar a:last-child{border-right:none}
.site-footer{position:absolute;left:0;top:2204px;width:1200px;height:340px;background:var(--footer);text-align:center;color:var(--footer-text)}
.footer-brand{display:inline-flex;align-items:center;gap:12px;margin-top:90px;color:var(--white);font-family:"Roboto Condensed",sans-serif;font-weight:700;font-size:38px;letter-spacing:1px}
.footer-brand .brand-mark{width:16px;height:16px}
.footer-nav{margin-top:26px;display:flex;justify-content:center;gap:20px}
.footer-nav a{color:#d8d8d8;font-size:11px;font-weight:600;text-decoration:none}
.footer-note{margin:26px auto 0;width:760px;font-size:11.5px;line-height:18px}
.footer-rule{width:1080px;margin:30px auto 0;border-top:1px solid #3d3d3d}
.copyright{margin-top:18px;font-size:11px}
</style>
</head>
<body>

<section class="hero">
  <div class="hero-media" role="img" aria-label="Blue-toned photograph of a business meeting"></div>
  <header class="site-header">
    <div class="brand"><span class="brand-mark"></span>TLK Ventures</div>
    <nav class="main-nav">
      <a href="#">PROFILE</a><a href="#">TEAM</a><a href="#">APPROACH</a><a href="#">CONTACT</a><a href="#">NEWS</a><a href="#">PORTFOLIO</a>
    </nav>
    <div class="utility"><a href="#">SITE MAP</a><a href="#">DISCLAIMER</a></div>
  </header>
  <div class="hero-card">
    <div class="hero-title">EVOLVE LEAD</div>
    <p class="hero-text">Lorem Ipsum has been the industry's standard dummy text ever since the 1500s when an unknown printer took a galley of type and scrambled it to make a type book.</p>
    <a class="hero-btn" href="#">READ MORE</a>
  </div>
  <div class="hero-dots"><span></span><span></span><span></span></div>
</section>

<section class="latest">
  <div class="section-head" style="top:62px">
    <span class="section-icon"><svg width="18" height="18" viewBox="0 0 18 18"><circle cx="9" cy="9" r="7" fill="none" stroke="#fff" stroke-width="2"/><path d="M9 5v4l3 2" stroke="#fff" stroke-width="2" fill="none"/></svg></span>
    <h2 class="section-title">The Latest</h2>
  </div>
  <span class="see-all">See all</span>
  <div class="latest-row">
    <article class="latest-card"><div class="thumb" role="img" aria-label="Photo of a crowd at a public gathering" style="background:linear-gradient(135deg,#8fa3b8,#c9b79a)"></div><p class="latest-meta">Markets</p><p class="latest-text">Lorem Ipsum has been the industry's standard dummy text ever since the 1500s, when an unknown printer.</p></article>
    <article class="latest-card"><div class="thumb" role="img" aria-label="Photo of a street rally with banners" style="background:linear-gradient(135deg,#b9a48c,#7f8f9e)"></div><p class="latest-meta">Policy</p><p class="latest-text">Lorem Ipsum has been the industry's standard dummy text ever since the 1500s, when an unknown printer.</p></article>
    <article class="latest-card"><div class="thumb" role="img" aria-label="Photo of a speaker at a podium" style="background:linear-gradient(135deg,#6f6a64,#b58d6e)"></div><p class="latest-meta">Deals</p><p class="latest-text">Lorem Ipsum has been the industry's standard dummy text ever since the 1500s, when an unknown printer.</p></article>
    <article class="latest-card"><div class="thumb" role="img" aria-label="Photo of a city skyline" style="background:linear-gradient(135deg,#9fb4c7,#d9d3c6)"></div><p class="latest-meta">3 hours ago</p><p class="latest-text">Lorem Ipsum has been the industry's standard dummy text ever since the 1500s, when an unknown printer.</p></article>
    <article class="latest-card"><div class="thumb" role="img" aria-label="Photo of a busy market street" style="background:linear-gradient(135deg,#b88a62,#8c7361)"></div><p class="latest-meta">2 days ago</p><p class="latest-text">Lorem Ipsum has been the industry's standard dummy text ever since the 1500s, when an unknown printer.</p></article>
  </div>
</section>

<section class="news">
  <div class="section-head" style="top:86px">
    <span class="section-icon"><svg width="16" height="16" viewBox="0 0 16 16"><path d="M4 2l10 6-10 6z" fill="#fff"/></svg></span>
    <h2 class="section-title">News &amp; Events</h2>
  </div>
  <div class="news-grid">
    <article class="news-item"><div class="thumb" role="img" aria-label="Photo of a business event" style="background:linear-gradient(135deg,#7e8ea3,#c2b3a0)"></div><p class="news-text">Lorem Ipsum has been the industry's standard dummy text ever since the 1500s, when an unknown printer took a galley.</p></article>
    <article class="news-item"><div class="thumb" role="img" aria-label="Video still of a panel discussion" style="background:linear-gradient(135deg,#5d6e82,#a38c7a)"><span class="play"><svg width="12" height="12" viewBox="0 0 12 12"><path d="M3 1l8 5-8 5z" fill="#fff"/></svg></span></div><p class="news-text">Lorem Ipsum has been the industry's standard dummy text ever since the 1500s, when an unknown printer took a galley.</p></article>
    <article class="news-item"><div class="thumb" role="img" aria-label="Photo of a conference audience" style="background:linear-gradient(135deg,#6f5f55,#b49a82)"></div><p class="news-text">Lorem Ipsum has been the industry's standard dummy text ever since the 1500s, when an unknown printer took a galley.</p></article>
    <article class="news-item"><div class="thumb" role="img" aria-label="Photo of a sports ground" style="background:linear-gradient(135deg,#8aa07a,#c7c1a8)"></div><p class="news-text">Lorem Ipsum has been the industry's standard dummy text ever since the 1500s, when an unknown printer took a galley.</p></article>
    <article class="news-item"><div class="thumb" role="img" aria-label="Photo of a speaker addressing an audience" style="background:linear-gradient(135deg,#4d5d74,#9f7f6a)"></div><p class="news-text">Lorem Ipsum has been the industry's standard dummy text ever since the 1500s, when an unknown printer took a galley.</p></article>
    <article class="news-item"><div class="thumb" role="img" aria-label="Photo of an office interior" style="background:linear-gradient(135deg,#a9b6c4,#6f7f90)"></div><p class="news-text">Lorem Ipsum has been the industry's standard dummy text ever since the 1500s, when an unknown printer took a galley.</p></article>
  </div>
  <div class="load-more">LOAD MORE</div>
</section>

<section class="portfolio">
  <div class="section-head" style="top:30px">
    <span class="section-icon"><svg width="18" height="16" viewBox="0 0 18 16"><path d="M1 3h6l2 2h8v10H1z" fill="#fff"/></svg></span>
    <h2 class="section-title">Our Portfolio</h2>
  </div>
  <svg class="arrow" style="left:22px" width="16" height="26" viewBox="0 0 16 26"><path d="M16 0v26L0 13z" fill="#333"/></svg>
  <svg class="arrow" style="right:22px" width="16" height="26" viewBox="0 0 16 26"><path d="M0 0v26l16-13z" fill="#333"/></svg>
  <div class="portfolio-row">
    <div class="company"><div class="company-mark"><i></i>Ninearc Media</div><p class="company-name">Ninearc Media Pvt. Ltd.</p><p class="company-sector">Consumer Services</p></div>
    <div class="company"><div class="company-mark"><i></i>Crestline</div><p class="company-name">Crestline Telecom Infrastructure Private Limited</p><p class="company-sector">Infrastructure Telecommunications and Information Technology</p></div>
    <div class="company"><div class="company-mark"><i></i>Amberleaf</div><p class="company-name">Amberleaf Lifesciences Ltd.</p><p class="company-sector">Manufacturing and Engineering</p></div>
    <div class="company"><div class="company-mark"><i></i>Torus Rings</div><p class="company-name">Torus Rings Pvt. Ltd.</p><p class="company-sector">Manufacturing and Engineering</p></div>
    <div class="company"><div class="company-mark"><i></i>Orvan</div><p class="company-name">Orvan Communications Ltd.</p><p class="company-sector">Consumer Services Telecommunications and Information Technology</p></div>
  </div>
</section>

<nav class="social-bar">
  <a href="#">FACENOTE</a><a href="#">CHIRPER</a><a href="#">CIRCLES PLUS</a><a href="#">LINKPRO</a><a href="#">PINWALL</a>
</nav>

<footer class="site-footer">
  <div class="footer-brand"><span class="brand-mark"></span>TLK Ventures</div>
  <nav class="footer-nav"><a href="#">PROFILE</a><a href="#">TEAM</a><a href="#">APPROACH</a><a href="#">CONTACT</a><a href="#">NEWS</a><a href="#">PORTFOLIO</a></nav>
  <p class="footer-note">TLK Ventures LLC is supported by an experienced team of investment professionals at TLK Advisors Pvt. Ltd. in India and TLK Advisors (Dubai) Limited in the Middle East.</p>
  <div class="footer-rule"></div>
  <p class="copyright">© 2017 TLK Ventures. All rights reserved.</p>
</footer>

</body>
</html>
```